Stationery and Business Cards
PulseHaven
Bright & Fun-filled
Tessa Lund
Massage Therapist
42 Caxbury Vale Road
London
e4 8QT
massage@pulsehaven.co.uk
www.pulsehaven.co.uk

```html
<!DOCTYPE html>
<html lang="en">
<head>
<meta charset="utf-8">
<title>PulseHaven Stationery</title>
<link href="https://fonts.googleapis.com/css2?family=Montserrat:wght@400;600;800&display=swap" rel="stylesheet">
<style>
  :root {
    --navy: #1b2f4f;
    --green: #a8d5b2;
    --green-deep: #5caa74;
    --paper: #ffffff;
    --ground: #e9ebee;
    --muted: #6b7686;
  }
  * { margin: 0; padding: 0; box-sizing: border-box; }
  html, body { width: 1200px; height: 1011px; overflow: hidden; }
  body {
    background: var(--ground);
    font-family: "Montserrat", Arial, sans-serif;
    color: var(--navy);
    position: relative;
  }
  .sheet {
    position: absolute;
    background: var(--paper);
    box-shadow: 0 4px 14px rgba(20, 30, 50, 0.18);
    overflow: hidden;
  }
  .wave-band {
    position: absolute;
    left: 0;
    width: 100%;
    background: linear-gradient(180deg, rgba(168, 213, 178, 0) 0%, rgba(168, 213, 178, 0.55) 45%, rgba(27, 47, 79, 0.18) 100%);
  }
  .brand {
    font-weight: 800;
    color: var(--navy);
    letter-spacing: -0.5px;
    line-height: 1;
    display: flex;
    align-items: center;
    gap: 6px;
    white-space: nowrap;
  }
  .brand-dot { border-radius: 50%; background: var(--green-deep); flex: none; }
  .tagline { color: var(--green-deep); font-weight: 400; white-space: nowrap; }
  .web { position: absolute; font-weight: 400; letter-spacing: 1.5px; color: var(--muted); white-space: nowrap; }

  /* Letterhead */
  .letterhead { left: 50px; top: 110px; width: 560px; height: 792px; }
  .letterhead .brand { position: absolute; left: 44px; top: 44px; font-size: 30px; }
  .letterhead .brand-dot { width: 12px; height: 12px; }
  .letterhead .tagline { position: absolute; left: 44px; top: 80px; font-size: 10px; }
  .letterhead .address {
    position: absolute; right: 44px; top: 44px;
    font-size: 9.5px; line-height: 1.6; color: var(--navy); font-style: normal;
  }
  .letterhead .wave-band { bottom: 80px; height: 120px; }
  .letterhead .web { right: 44px; bottom: 26px; font-size: 11px; }

  /* Envelope */
  .envelope { left: 650px; top: 110px; width: 500px; height: 250px; }
  .envelope .brand { position: absolute; left: 26px; top: 24px; font-size: 20px; }
  .envelope .brand-dot { width: 9px; height: 9px; }
  .envelope .tagline { position: absolute; left: 26px; top: 48px; font-size: 8px; }
  .envelope .wave-band { bottom: 36px; height: 90px; }
  .envelope .web { right: 24px; bottom: 10px; font-size: 8.5px; }

  /* Business card back */
  .card { width: 245px; height: 155px; }
  .card-back { left: 650px; top: 400px; background: var(--navy); }
  .card-back .brand { position: absolute; left: 0; right: 0; top: 58px; justify-content: center; font-size: 20px; color: var(--paper); }
  .card-back .brand-dot { width: 9px; height: 9px; background: var(--green); }
  .card-back .web { left: 0; right: 0; bottom: 16px; text-align: center; font-size: 8px; color: var(--green); }

  /* Small note card */
  .card-note { left: 905px; top: 400px; }
  .card-note .brand { position: absolute; left: 22px; top: 40px; font-size: 18px; }
  .card-note .brand-dot { width: 8px; height: 8px; }
  .card-note .tagline { position: absolute; left: 22px; top: 62px; font-size: 7.5px; }
  .card-note .web { left: 22px; bottom: 16px; font-size: 8px; }

  /* Business card front */
  .card-front { left: 777px; top: 600px; }
  .card-front .brand { position: absolute; left: 12px; top: 16px; font-size: 14px; gap: 4px; }
  .card-front .brand-dot { width: 6px; height: 6px; }
  .card-front .tagline { position: absolute; left: 12px; top: 34px; font-size: 6px; }
  .card-front .person { position: absolute; left: 134px; top: 16px; font-size: 6.5px; line-height: 1.5; }
  .card-front .person-name { font-weight: 600; font-size: 8.5px; }
  .card-front .person-role { color: var(--green-deep); margin-bottom: 2px; }
  .card-front .wave-band { bottom: 20px; height: 30px; }
  .card-front .web { right: 12px; bottom: 6px; font-size: 6.5px; }
</style>
</head>
<body>

<section class="sheet letterhead">
  <div class="brand">PulseHaven<span class="brand-dot"></span></div>
  <div class="tagline">sports &amp; relaxation massage therapy</div>
  <address class="address">
    42 Caxbury Vale Road<br>London, e4 8QT<br><br>
    T: 07700 900412<br>
    E: massage@pulsehaven.co.uk
  </address>
  <div class="wave-band" role="img" aria-label="Decorative green and navy wave artwork"></div>
  <div class="web">www.pulsehaven.co.uk</div>
</section>

<section class="sheet envelope">
  <div class="brand">PulseHaven<span class="brand-dot"></span></div>
  <div class="tagline">sports &amp; relaxation massage therapy</div>
  <div class="wave-band" role="img" aria-label="Decorative green and navy wave artwork"></div>
  <div class="web">www.pulsehaven.co.uk</div>
</section>

<section class="sheet card card-back">
  <div class="brand">PulseHaven<span class="brand-dot"></span></div>
  <div class="web">www.pulsehaven.co.uk</div>
</section>

<section class="sheet card card-note">
  <div class="brand">PulseHaven<span class="brand-dot"></span></div>
  <div class="tagline">sports &amp; relaxation massage therapy</div>
  <div class="web">www.pulsehaven.co.uk</div>
</section>

<section class="sheet card card-front">
  <div class="brand">PulseHaven<span class="brand-dot"></span></div>
  <div class="tagline">sports &amp; relaxation massage</div>
  <div class="person">
    <div class="person-name">Tessa Lund</div>
    <div class="person-role">Massage Therapist</div>
    42 Caxbury Vale Road<br>London, e4 8QT<br>
    07700 900412<br>massage@pulsehaven.co.uk
  </div>
  <div class="wave-band" role="img" aria-label="Decorative green and navy wave artwork"></div>
  <div class="web">www.pulsehaven.co.uk</div>
</section>

</body>
</html>
```